Creative Challenge - Disruptive Digital Construction Business needs an Application Design

We need an application design (4 screens).
The app will offer easy-to-use an interactive course to illustrate the latest technology to construction professionals. Kindly find the attachments.
Updates

I have just posted the contest and the deadline is tomorrow!! Please give me my original 7 days back.

Need extra days to review

Target Market(s)

Construction professionals, aged from 22 to 36, who want to learn new disruptive technologies in construction.

Colors
e667a6
b868aa
33a6d7

Requirements
Must have
• The name of the app, Velunor, stands for “Brightframe Skill Voyagers”. The user is a Velunor, who would transform the digital construction industry. We want a design that gives that feel to the users.

```html
<!DOCTYPE html>
<html lang="en">
<head>
<meta charset="utf-8">
<title>Velunor – App Screens</title>
<link href="https://fonts.googleapis.com/css2?family=Crimson+Pro:wght@400;500&family=Mulish:wght@400;600&display=swap" rel="stylesheet">
<style>
:root{
  --canvas:#e4e2ec;
  --navy:#22234a;
  --pink:#e667a6;
  --magenta:#b868aa;
  --sky:#33a6d7;
  --accent-grad:linear-gradient(90deg,var(--magenta),var(--pink));
  --lavender:#e6e2f3;
  --screen-light:#f4f4f7;
  --ice:#eaf4f9;
  --ink:#2b2c45;
  --muted:#7b7c92;
  --white:#ffffff;
}
*{box-sizing:border-box;margin:0;padding:0}
html,body{width:1200px;height:900px;overflow:hidden}
body{background:var(--canvas);font-family:"Mulish",sans-serif;color:var(--ink);position:relative}
.serif{font-family:"Crimson Pro",serif}
.screen{position:absolute;width:166px;height:362px;border-radius:20px;overflow:hidden;background:var(--screen-light);box-shadow:0 6px 18px rgba(60,60,90,.12)}
.abs{position:absolute}
.status{position:absolute;top:6px;left:12px;right:12px;font-size:6px;display:flex;justify-content:space-between}
.status .bars{display:flex;gap:2px;align-items:center}
.status .bars i{display:block;width:8px;height:3px;background:currentColor;border-radius:1px}
.center{left:0;right:0;text-align:center}

/* onboarding */
.onboard{left:60px;top:52px}
.onboard .photo{inset:0;background:linear-gradient(180deg,#6c8896 0%,#55727e 35%,#34405a 62%,var(--navy) 100%)}
.onboard .status,.welcome .status,.signin .status{color:var(--white)}
.onboard .headline{top:214px;font-size:9.5px;color:var(--white);line-height:1.35;padding:0 16px}
.onboard .sub{top:258px;font-size:5.5px;color:#e6e6f0;line-height:1.3;padding:0 20px}
.dots{top:301px;display:flex;justify-content:center;align-items:center;gap:6px}
.dots i{width:4px;height:4px;border-radius:50%;background:#9a9cb8}
.dots i.on{width:5px;height:5px;background:var(--pink)}
.skip{right:10px;top:327px;font-size:5.5px;color:var(--white)}

/* welcome */
.welcome{left:361px;top:52px}
.welcome .photo{inset:0;background:linear-gradient(180deg,#9aa1b4 0%,#5c6288 40%,#36396a 70%,var(--navy) 100%)}
.welcome h1{top:226px;font-size:16px;font-weight:400;color:var(--white)}
.welcome .sub{top:256px;font-size:5.5px;color:var(--white);line-height:1.45}
.btn{position:absolute;height:19px;font-size:7px;display:flex;align-items:center;justify-content:center;color:var(--white)}
.btn.fill{background:var(--accent-grad)}
.btn.ghost{border:1px solid #d9bcd4}

/* sign in */
.signin{left:662px;top:60px}
.signin .photo{inset:0;background:linear-gradient(180deg,#e6e6ec 0%,#b7b8c6 30%,#6e7190 58%,#3a3d6a 80%,var(--navy) 100%)}
.signin .name{top:62px;left:10px;font-size:16px;color:var(--white)}
.signin .back{top:92px;left:10px;font-size:10px;color:var(--white)}
.field-label{left:10px;font-size:6.5px;color:#efd9ea}
.field-value{left:10px;font-size:6px;color:var(--white)}
.underline{left:10px;right:10px;height:1px;background:var(--magenta)}
.forgot{right:10px;top:190px;font-size:4.5px;color:#f3b6d4}
.divider{top:256px;left:10px;right:10px;display:flex;align-items:center;gap:5px;font-size:5.5px;color:var(--white)}
.divider span{flex:1;height:1px;background:#9597b8}
.social{top:280px;left:0;right:0;display:flex;justify-content:center;gap:26px}
.social i{width:18px;height:18px;border:1px solid #d5d6ea;border-radius:50%;font-style:normal;font-size:3.6px;color:var(--white);display:flex;align-items:center;justify-content:center}
.member{top:312px;font-size:5.5px;color:var(--white)}
.member b{font-weight:400;color:var(--pink)}

/* home */
.home{left:964px;top:56px}
.home .status,.dark-status{color:var(--ink)}
.home .hello{top:20px;left:18px;font-size:8.5px}
.resource-head{top:40px;left:15px;right:15px;height:22px;background:var(--white);display:flex;align-items:center;font-size:6px;box-shadow:0 1px 3px rgba(0,0,0,.06)}
.pill{background:var(--sky);color:var(--white);font-size:7px;padding:4px 8px;margin:0 9px 0 5px}
.resource-list{top:62px;left:15px;right:15px;height:86px;background:var(--ice);padding:8px 0 0 6px}
.resource-list li{list-style:none;font-size:6px;line-height:12.8px;display:flex;align-items:center;gap:5px}
.resource-list li::before{content:"";width:5px;height:1px;background:var(--ink)}
.home .continue{top:173px;left:18px;font-size:8px}
.reading{top:191px;left:15px;right:15px;height:60px;background:var(--lavender);padding:8px 8px 0}
.reading .t{font-size:7.5px;border-left:1px solid var(--magenta);padding-left:3px}
.reading .meta{font-size:5.5px;margin-top:10px}
.reading .row{display:flex;justify-content:space-between;font-size:5.5px;margin-top:2px}
.track{height:1.5px;background:#dcc9e0;margin-top:7px;position:relative}
.track i{position:absolute;left:0;top:0;height:100%;width:10%;background:var(--accent-grad)}
.promo-art{top:270px;left:28px;width:30px;height:36px;background:linear-gradient(180deg,#d6e6f0,var(--magenta));border-radius:3px}
.promo-text{top:272px;left:74px;font-size:5px;line-height:1.45}
.explore-sm{top:293px;left:74px;width:47px;height:11px;border:1px solid #9a9bb2;font-size:4.5px;display:flex;align-items:center;justify-content:center}
.tabbar{left:0;right:0;bottom:0;height:28px;background:var(--white);display:flex;justify-content:space-around;align-items:center;border-top:1px solid #ececf2}
.tab{display:flex;flex-direction:column;align-items:center;font-size:3.6px;color:var(--muted);gap:1px}
.tab.on{color:var(--pink)}

/* modules */
.modules{left:199px;top:486px}
.modules .title{top:27px;left:14px;font-size:8.5px;font-weight:500}
.module{position:absolute;left:14px;right:14px;height:22px;background:var(--white);border-right:2px solid var(--magenta);display:flex;align-items:center;font-size:6.5px;color:var(--ink);box-shadow:0 1px 2px rgba(0,0,0,.05)}
.module.on{background:var(--lavender);border:1px solid #d3b8d8;border-right:2px solid var(--magenta)}
.module .num{position:absolute;left:0;top:0;width:18px;height:18px;background:#e6dbec;border-radius:0 0 18px 0;font-size:4.5px;padding:3px 0 0 4px}
.module .name{margin-left:26px}

/* module detail */
.detail{left:521px;top:481px}
.detail .band{left:0;right:0;top:0;height:120px;background:var(--lavender)}
.detail .status{color:var(--ink)}
.backbtn{top:21px;left:7px;width:9px;height:9px;border-radius:50%;background:#6f7088}
.detail .num{top:36px;left:20px;font-size:7.5px}
.detail .h{top:48px;left:20px;font-size:8px}
.detail .para{top:64px;left:20px;right:12px;font-size:6.3px;line-height:1.35;color:#3f4060}
.timeline{top:131px;bottom:0;left:21px;width:0;border-left:1px dashed #7d7e98}
.step{position:absolute;left:27px;right:10px;font-size:6px;line-height:1.35}
.step::before{content:"";position:absolute;left:-8px;top:2px;width:3px;height:3px;border-radius:50%;background:var(--magenta)}
.step.first::before{width:5px;height:5px;left:-9px;top:1px;background:var(--pink);box-shadow:0 0 0 1.5px #f3c9de}
.mini-btn{position:absolute;height:12px;font-size:5.5px;display:flex;align-items:center;justify-content:center}

/* lesson */
.lesson{left:844px;top:477px}
.lesson .photo{left:0;right:0;top:0;height:93px;background:linear-gradient(135deg,#8a5b48 0%,#c6c2bd 45%,#e8e7e4 100%)}
.lesson .status{color:var(--ink)}
.play{top:41px;left:78px;width:9px;height:9px;border-radius:50%;background:rgba(255,255,255,.85)}
.lesson .card{top:101px;left:7px;right:7px;height:178px;background:var(--white);box-shadow:0 1px 3px rgba(0,0,0,.05)}
.lesson .lead{top:8px;left:0;font-size:6.3px;line-height:1.35;border-left:1.5px solid var(--magenta);padding-left:7px;padding-right:10px}
.lesson .p{left:7px;right:10px;font-size:6px;line-height:1.4;color:#3f4060}
.lesson .start{right:7px;bottom:7px;font-size:5.5px}
.lesson .att{top:298px;left:14px;font-size:6.5px}
.attach{position:absolute;left:7px;right:7px;height:17px;background:var(--white);display:flex;align-items:center;font-size:6.3px;padding:0 8px;gap:6px}
.attach .ic{width:5px;height:7px;background:var(--sky)}
.attach .dl{margin-left:auto}
</style>
</head>
<body>

<!-- Onboarding -->
<section class="screen onboard">
  <div class="abs photo" role="img" aria-label="Photo of a building under construction with scaffolding and rebar columns"></div>
  <div class="status"><span>9:41</span><span class="bars"><i></i></span></div>
  <p class="abs center headline serif">Lorem dolor sit amet consectetur adipisicing elit</p>
  <p class="abs center sub">Lorem dolor sit amet consectetur adipisicing eli sed do eiusmod tempor</p>
  <div class="abs center dots"><i></i><i class="on"></i><i></i><i></i></div>
  <span class="abs skip">skip</span>
</section>

<!-- Welcome -->
<section class="screen welcome">
  <div class="abs photo" role="img" aria-label="Photo of a professional working at a desk"></div>
  <div class="status"><span>9:41</span><span class="bars"><i></i></span></div>
  <h1 class="abs center serif">Welcome</h1>
  <p class="abs center sub">Please login or sign up to continue<br>using this app</p>
  <div class="btn fill" style="left:18px;top:300px;width:60px">Login</div>
  <div class="btn ghost" style="left:89px;top:300px;width:60px">Signup</div>
</section>

<!-- Sign in -->
<section class="screen signin">
  <div class="abs photo" role="img" aria-label="Photo of a hand writing with a pen on paper"></div>
  <div class="status"><span>9:41</span><span class="bars"><i></i></span></div>
  <p class="abs name serif">Velunor</p>
  <p class="abs back">Welcome back!</p>
  <span class="abs field-label" style="top:125px">Email</span>
  <span class="abs field-value" style="top:140px">username@mail.com</span>
  <svg class="abs" style="right:10px;top:139px" width="7" height="7" viewBox="0 0 10 10"><circle cx="5" cy="3" r="2.3" fill="#fff"/><path d="M1 10c0-3 2-4.5 4-4.5S9 7 9 10z" fill="#fff"/></svg>
  <div class="abs underline" style="top:151px"></div>
  <span class="abs field-label" style="top:160px">Password</span>
  <span class="abs field-value" style="top:173px;letter-spacing:1px">••••••••••</span>
  <svg class="abs" style="right:10px;top:175px" width="10" height="6" viewBox="0 0 12 7"><path d="M0 3.5C2 .5 10 .5 12 3.5 10 6.5 2 6.5 0 3.5z" fill="#fff"/><circle cx="6" cy="3.5" r="1.5" fill="#5c5f86"/></svg>
  <div class="abs underline" style="top:186px"></div>
  <span class="abs forgot">Forgot Password?</span>
  <div class="btn fill" style="left:10px;right:10px;top:213px">Login</div>
  <div class="abs divider"><span></span>Or Signup With<span></span></div>
  <div class="abs social"><i>Linkora</i><i>Chirpline</i><i>Seekwell</i></div>
  <p class="abs center member">New Member? <b>Sign up</b></p>
</section>

<!-- Home -->
<section class="screen home">
  <div class="status"><span>9:41</span><span class="bars"><i></i></span></div>
  <p class="abs hello serif">Hello User!</p>
  <div class="abs resource-head"><span class="pill">New</span>Explore 6 more resources
    <svg style="margin-left:10px" width="6" height="4" viewBox="0 0 6 4"><path d="M.5 3.5 3 1l2.5 2.5" stroke="#2b2c45" fill="none"/></svg></div>
  <ul class="abs resource-list">
    <li>Refrences</li><li>BIM Related Standards</li><li>Abbreviations</li><li>Useful Links</li><li>Quality Ckecks</li><li>BIM Software</li>
  </ul>
  <p class="abs continue serif">Continue Reading</p>
  <div class="abs reading">
    <p class="t serif">BIM Project Management</p>
    <p class="meta">02</p>
    <div class="row"><span>Invitation to Tender</span><span>Progress: 10%</span></div>
    <div class="track"><i></i></div>
  </div>
  <div class="abs promo-art" role="img" aria-label="Illustration of a professional beside a large phone"></div>
  <p class="abs promo-text">Learn new disruptive<br>technology in construction.</p>
  <div class="abs explore-sm">Explore more</div>
  <nav class="abs tabbar">
    <span class="tab on"><svg width="10" height="9" viewBox="0 0 10 9"><path d="M5 0 0 4h1.3v5h2.7V6h2v3h2.7V4H10z" fill="#e667a6"/></svg>Home</span>
    <span class="tab"><svg width="8" height="9" viewBox="0 0 8 9"><rect x=".5" y=".5" width="7" height="8" fill="none" stroke="#7b7c92"/></svg>Resources</span>
    <span class="tab"><svg width="11" height="9" viewBox="0 0 11 9"><path d="M.5 1h4l1 1 1-1h4v7h-4l-1 .8-1-.8h-4z" fill="none" stroke="#7b7c92"/></svg>Activities</span>
    <span class="tab"><svg width="9" height="9" viewBox="0 0 9 9"><circle cx="4.5" cy="2.5" r="2" fill="none" stroke="#7b7c92"/><path d="M.5 9c0-3 2-4 4-4s4 1 4 4" fill="none" stroke="#7b7c92"/></svg>Profile</span>
  </nav>
</section>

<!-- Module list -->
<section class="screen modules">
  <div class="status dark-status"><span>9:41</span><span class="bars"><i></i></span></div>
  <p class="abs title serif">BIM Project Management</p>
  <div class="module on" style="top:49px"><span class="num">01</span><span class="name">Assessment &amp; Needs</span></div>
  <div class="module" style="top:77px"><span class="num">02</span><span class="name">Invitation to Tender</span></div>
  <div class="module" style="top:104px"><span class="num">03</span><span class="name">Tender Response</span></div>
  <div class="module" style="top:132px"><span class="num">04</span><span class="name">Appointment</span></div>
  <div class="module" style="top:160px"><span class="num">05</span><span class="name">Mobilization</span></div>
  <div class="module" style="top:187px"><span class="num">06</span><span class="name">Collaborative Product of Information</span></div>
  <div class="module" style="top:215px"><span class="num">07</span><span class="name">Information Model Delivery</span></div>
  <div class="module" style="top:242px"><span class="num">08</span><span class="name">Project close-out</span></div>
</section>

<!-- Module detail -->
<section class="screen detail">
  <div class="abs band"></div>
  <div class="status"><span>9:41</span><span class="bars"><i></i></span></div>
  <div class="abs backbtn"></div>
  <p class="abs num">01</p>
  <p class="abs h serif">Assessment &amp; Needs</p>
  <p class="abs para">Lorem ipsum dolor sit amet, consetetur sadipscing elitr, sed diam nonumy eirmod tempor invidunt ut labore et dolore magna aliquyam erat, sed diam voluptua. At vero eos et accusam et justo duo.</p>
  <div class="abs timeline"></div>
  <p class="step first" style="top:132px">Appoint Individuals to undertake the information management function</p>
  <p class="abs" style="top:154px;left:41px;font-size:5px">Progress: 10%</p>
  <div class="abs" style="top:162px;left:37px;width:99px;height:2px;background:#dcc9e0"><div style="width:12%;height:100%;background:var(--accent-grad)"></div></div>
  <div class="mini-btn" style="top:173px;left:40px;width:39px;background:var(--accent-grad);color:#fff">Explore</div>
  <div class="mini-btn" style="top:173px;left:90px;width:45px;border:1px solid #a9aabe;color:var(--muted)">Download</div>
  <p class="step" style="top:215px">Establish the project's information requirements</p>
  <p class="step" style="top:247px">Establish the project's information delivery milestones</p>
  <p class="step" style="top:280px">Establish the project's information standards</p>
  <p class="step" style="top:311px">Establish the project's information production methods and procedures</p>
  <p class="step" style="top:340px">Establish the project's reference information and shared resources</p>
</section>

<!-- Lesson -->
<section class="screen lesson">
  <div class="abs photo" role="img" aria-label="Video still of a teacher presenting at a whiteboard"></div>
  <div class="status"><span>9:41</span><span class="bars"><i></i></span></div>
  <div class="abs play"></div>
  <div class="abs card">
    <p class="abs lead serif">Appoint Individuals to undertake the information management function.</p>
    <p class="abs p" style="top:34px">Lorem ipsum dolor sit amet, consetetur sadipscing elitr, sed diam nonumy eirmod tempor invidunt.</p>
    <p class="abs p" style="top:67px">ut labore et dolore magna aliquyam erat, sed diam voluptua. At vero eos et accusam et justo duo dolores et ea rebum. Stet clita kasd gubergren, no sea takimata sanctus.</p>
    <p class="abs p" style="top:109px">Lorem ipsum dolor sit amet, consetetur sadipscing elitr, sed diam nonumy eirmod tempor invidunt ut labore et dolore magna aliquyam erat, sed diam voluptua. At vero eos et accusam et justo duo.</p>
    <span class="abs start">Start →</span>
  </div>
  <p class="abs att serif">Attachments</p>
  <div class="attach" style="top:308px"><span class="ic"></span>Lorem ipsum dolor sit amet<svg class="dl" width="7" height="7" viewBox="0 0 8 8"><path d="M4 0v5M2 3l2 2 2-2M.5 6v1.5h7V6" stroke="#b868aa" fill="none"/></svg></div>
  <div class="attach" style="top:329px"><span class="ic"></span>Lorem ipsum dolor sit amet<svg class="dl" width="7" height="7" viewBox="0 0 8 8"><path d="M4 0v5M2 3l2 2 2-2M.5 6v1.5h7V6" stroke="#b868aa" fill="none"/></svg></div>
</section>

</body>
</html>
```